Exciting adult social quiz app needs awesome modern design

A new and exciting app for couples/sexual partners is in the making. It will be available for Orvane and Quillo devices and allow one partner to invite another partner to the game. The partners will answer questions about their sexual desires and needs and then try to guess what the other one answered.

The app needs a high quality design and you can find some general inspiration in a similar social quiz app called "Pear Trail" which can be found in Gadget Depot and Fetch Market. I like some of the basic layouts of this app.

The design should be classy and have a theme that matches the app subject. This is a sexual get-to-know-each-other-app and not a "porn app". I imagine colors might be black and red (not a requirement) and perhaps have some structures, pictures or backgrounds showing a bit of skin. It's important that the game can be accessed by players in the public space (e.g. in a bus, car etc.) without surroundings thinking it's a sex/porn game - but also important that it's exciting in a kind of sexual way. So try to find a fine line.

As the app is for both genders, the design should accommodate this.

Please see app mockups in the attached PDF.

Initially, please show design proposals for screens 13, 16 and 23.
Please notice that screen 16 doesn't have to be exactly those 2 bars - please make some alternative score comparison graphic in your proposal.

Looking forward to seeing your proposal soon!

Target Market(s)

Couples between 18 and 50

Industry/Entity Type

Adult

Requirements
Must have
• Smooth graphics like the app "Pear Trail"
Nice to have
• Several proposals are appreciated. Perhaps you can show your proposals with different colors and object placements so that I can see some different options.

```html
<!DOCTYPE html>
<html lang="en">
<head>
<meta charset="utf-8">
<title>Round 1 – Sexual Favour</title>
<link rel="stylesheet" href="https://fonts.googleapis.com/css2?family=Lilita+One&family=Signika:wght@700&display=swap">
<style>
  :root {
    --bg-deep: #4a0000;
    --bg-mid: #7d0606;
    --bg-glow: #9a1010;
    --header: #7a0000;
    --ring: #9b0d0d;
    --symbol: #8a0b0b;
    --gold: #c9a458;
    --white: #ffffff;
    --title-top: #ffffff;
    --title-bottom: #e9ef6a;
    --title-edge: #2a0000;
    --pose-red: #ff1020;
    --pose-pale: #e4d6d6;
    --button-dark: #5e0000;
    --button-red: #a80e0e;
    --silver-light: #ffffff;
    --silver-dark: #b9b9b9;
    --ad-blue: #0000ff;
  }
  * { box-sizing: border-box; margin: 0; padding: 0; }
  html, body { width: 700px; height: 1200px; overflow: hidden; background: var(--bg-deep); }
  .screen {
    position: relative; width: 700px; height: 1200px; overflow: hidden;
    background: radial-gradient(ellipse at 45% 45%, var(--bg-glow) 0%, var(--bg-mid) 40%, var(--bg-deep) 100%);
    font-family: "Signika", "Trebuchet MS", sans-serif; color: var(--white);
  }
  .backdrop-figure {
    position: absolute; left: 430px; top: 130px; width: 270px; height: 1000px;
    background: radial-gradient(ellipse at 60% 30%, rgba(200,110,110,.35), rgba(120,30,30,0) 70%);
  }
  .round-header {
    position: absolute; left: 0; top: 0; width: 700px; height: 130px;
    background: linear-gradient(var(--header), #6a0000);
    display: flex; justify-content: center; align-items: center;
  }
  .round-title {
    font-family: "Lilita One", "Arial Black", sans-serif; font-size: 88px; letter-spacing: 4px;
    line-height: 1; margin-top: -10px;
    color: var(--title-bottom);
    background: linear-gradient(var(--title-top) 35%, var(--title-bottom));
    -webkit-background-clip: text; background-clip: text; -webkit-text-fill-color: transparent;
    filter: drop-shadow(0 0 0 var(--title-edge)) drop-shadow(3px 3px 0 var(--title-edge)) drop-shadow(-3px -3px 0 var(--title-edge)) drop-shadow(3px -3px 0 var(--title-edge)) drop-shadow(-3px 3px 0 var(--title-edge));
  }
  .header-rule {
    position: absolute; left: 80px; top: 131px; width: 540px; height: 2px;
    background: linear-gradient(90deg, transparent, var(--gold), transparent);
  }
  .round-rule {
    position: absolute; top: 190px; width: 700px; text-align: center;
    font-size: 35px; line-height: 50px; text-shadow: 0 2px 3px rgba(0,0,0,.4);
  }
  .gender-symbols { position: absolute; left: 0; top: 0; }
  .avatar {
    position: absolute; width: 90px; height: 90px; border-radius: 50%;
    background: linear-gradient(135deg, #7a8f6a, #c9b49a);
  }
  .avatar-him { left: 48px; top: 380px; }
  .avatar-her { left: 55px; top: 573px; background: linear-gradient(135deg, #5a3a30, #e0a8b8); }
  .pose {
    position: absolute; border-radius: 40px;
    border: 2px solid var(--gold);
  }
  .pose-him {
    left: 283px; top: 345px; width: 385px; height: 125px;
    background: linear-gradient(90deg, var(--pose-red) 0 34%, var(--pose-pale) 34%);
  }
  .pose-her {
    left: 292px; top: 535px; width: 370px; height: 150px;
    background: linear-gradient(90deg, var(--pose-red) 0 71%, var(--pose-pale) 71%);
  }
  .continue-button {
    position: absolute; left: 185px; top: 975px; width: 348px; height: 110px; border-radius: 55px;
    background: linear-gradient(var(--silver-light), var(--silver-dark));
    box-shadow: 0 0 0 4px rgba(120,60,60,.6);
    display: flex; justify-content: center; align-items: center;
  }
  .continue-button span {
    width: 288px; height: 66px; border-radius: 33px;
    background: linear-gradient(var(--button-red), var(--button-dark));
    display: flex; justify-content: center; align-items: center;
    font-size: 38px; color: var(--white);
  }
  .ad-slot {
    position: absolute; left: 110px; top: 1133px; width: 490px; height: 64px;
    background: var(--ad-blue); display: flex; justify-content: center; align-items: center;
    font-size: 36px;
  }
</style>
</head>
<body>
<main class="screen">
  <div class="backdrop-figure" role="img" aria-label="Soft red-toned background photo showing a bit of skin"></div>

  <header class="round-header"><h1 class="round-title">Round 1</h1></header>
  <div class="header-rule"></div>

  <p class="round-rule">Winner of the round<br>selects a sexual favour</p>

  <svg class="gender-symbols" width="700" height="1200" viewBox="0 0 700 1200" aria-hidden="true">
    <g stroke="var(--symbol)" stroke-width="14" stroke-linecap="round" fill="none">
      <line x1="140" y1="395" x2="240" y2="338"/>
      <polyline points="195,330 242,337 232,385"/>
      <line x1="100" y1="675" x2="100" y2="795"/>
      <line x1="58" y1="715" x2="143" y2="715"/>
    </g>
    <circle cx="93" cy="425" r="52" fill="none" stroke="var(--ring)" stroke-width="12"/>
    <circle cx="100" cy="618" r="52" fill="none" stroke="var(--ring)" stroke-width="12"/>
  </svg>

  <div class="avatar avatar-him" role="img" aria-label="Profile photo of the male player"></div>
  <div class="avatar avatar-her" role="img" aria-label="Profile photo of the female player"></div>

  <div class="pose pose-him" role="img" aria-label="Silhouette of a reclining man, partly highlighted in red"></div>
  <div class="pose pose-her" role="img" aria-label="Silhouette of a woman on all fours, mostly highlighted in red"></div>

  <div class="continue-button"><span>Continue</span></div>

  <div class="ad-slot">Ads here</div>
</main>
</body>
</html>
```